Event Planning Website

We are interested in redesigning our website. We just launched this company and we offer variety of event planning services. We specialize in wedding planning. We offer all inclusive packages, capturing the proposal, wedding planning, day of directing of the event. We help people save money, stay within budget and do the work so they could enjoy their special occasion.

We are looking to design 5 pages (we are open to suggestions to add or remove/combine), we like social media links (Facebook, instagram, yelp, testimonials) incorporated as recommended: Our existing webpage www.tendlanefest.com, Facebook.com/tendlanefest, http://instagram.com/tendlanefest, http://www.yelp.com/biz/tend-lane-fest-san-ramon, logo and flyer are attached. Please let us know if you need additional information. We are looking for a template to be able to easily edit, fill and embed content.

HOME PAGE
This is the landing page, we want it to be informative, attractive, effective leading to contact/lead.

SERVICES
This page should be about our services which we offer (proposal, planning, day of directing), all packages with clean layout detailing the packages.

MEDIA
This page will consist of photo gallery of past events, social media feed, video clips etc.

CONTACT
Modern, hip, minimalistic.

About us
Who we are, the team, bio about each planner within our firm, experience,

Industry/Entity Type

Event Planning

```html
<!DOCTYPE html>
<html lang="en">
<head>
<meta charset="utf-8">
<title>Tend Lane Fest — Gallery</title>
<link href="https://fonts.googleapis.com/css2?family=Didact+Gothic&family=Jost:wght@600&family=Open+Sans:wght@400;600;700&display=swap" rel="stylesheet">
<style>
:root{
  --ink:#1b1b1b;
  --header:#262626;
  --white:#ffffff;
  --accent:#4fd1b0;
  --rule:#5a5a5a;
  --btn-blue:#3b5a9a;
  --btn-sky:#2aa9e0;
  --footer-bg:#ffffff;
}
*{margin:0;padding:0;box-sizing:border-box}
html,body{width:854px;height:1200px;overflow:hidden;background:var(--white)}
body{position:relative;font-family:"Open Sans",sans-serif;color:var(--ink)}
.abs{position:absolute}

/* header */
.site-header{left:0;top:0;width:854px;height:65px;background:var(--header)}
.brand{left:32px;top:18px;display:flex;align-items:center;gap:8px;color:var(--white)}
.brand-mark{width:14px;height:14px;border:1.5px solid var(--white);border-radius:50%}
.brand-name{font-family:"Didact Gothic",sans-serif;font-size:19px;letter-spacing:.5px;line-height:1}
.brand-tag{left:54px;top:42px;font-family:"Didact Gothic",sans-serif;font-size:6px;letter-spacing:.6px;color:var(--white);text-transform:uppercase}
.main-nav{right:32px;top:27px;display:flex;gap:32px;font-family:"Didact Gothic",sans-serif;font-size:11.5px;color:var(--white)}
.main-nav .active{color:var(--accent)}

/* hero */
.hero{left:0;top:65px;width:854px;height:162px;background:linear-gradient(180deg,#3a3836 0%,#2c2a28 55%,#3f3c39 100%)}
.hero-title{left:130px;top:108px;height:24px;border-left:4px solid var(--accent);padding-left:17px;font-family:"Jost",sans-serif;font-weight:600;font-size:27px;line-height:24px;color:var(--white)}
.hero-intro{left:130px;top:145px;width:600px;font-size:8.6px;line-height:10.4px;color:var(--white)}

/* gallery */
.tile{width:191px;height:143px;overflow:hidden}
.tile-caption{left:0;bottom:0;width:100%;height:20px;background:rgba(0,0,0,.35);color:var(--white);font-size:9px;text-align:center;line-height:20px}
.heart{right:9px;top:10px;width:15px;height:13px}
.play{left:50%;top:50%;width:30px;height:30px;margin:-19px 0 0 -15px}
.tile-overlay{inset:0;background:rgba(20,16,14,.45);color:var(--white);text-align:center}
.tile-date{left:0;width:100%;top:38px;font-size:17px}
.tile-text{left:40px;width:111px;top:64px;font-size:9px;line-height:10.5px}
.tile-plus{left:86px;top:96px;width:18px;height:18px}
.arrow{width:14px;height:20px}

/* social */
.social{left:0;top:640px;width:854px;height:490px;background:radial-gradient(ellipse at 35% 35%,#2a1416 0%,#120c0c 45%,#070707 100%)}
.col-title{font-size:13px;font-weight:700;color:var(--white)}
.col-rule{height:1px;background:var(--rule)}
.col-divider{width:1px;background:var(--rule)}
.avatar{width:43px;height:33px}
.feed-text{font-size:9px;line-height:10.3px;color:var(--white)}
.btn{height:11px;padding:0 5px;font-size:7.5px;line-height:11px;color:var(--white);border-radius:1px}
.btn-share{background:var(--btn-blue)}
.btn-post{background:var(--btn-sky)}
.post-photo{width:112px;height:55px}
.stream-caption{left:0;bottom:0;width:100%;height:28px;background:rgba(255,255,255,.55);font-size:9px;line-height:28px;padding-left:11px;color:var(--ink)}

/* footer */
.site-footer{left:0;top:1130px;width:854px;height:70px;background:var(--footer-bg)}
.footer-nav{left:31px;top:22px;display:flex;gap:11px;font-family:"Didact Gothic",sans-serif;font-size:9.5px}
.copyright{right:32px;top:22px;font-family:"Didact Gothic",sans-serif;font-size:9.5px}
</style>
</head>
<body>

<header class="abs site-header">
  <div class="abs brand"><span class="brand-mark"></span><span class="brand-name">TEND LANE FEST</span></div>
  <div class="abs brand-tag">Planning &amp; Coordination</div>
  <nav class="abs main-nav">
    <span>HOME</span><span class="active">ABOUT</span><span>SERVICES</span><span>MEDIA</span><span>CONTACT</span>
  </nav>
</header>

<section class="abs hero" role="img" aria-label="Close-up photo of a couple's legs dancing on a brick pavement"></section>
<h1 class="abs hero-title">GALLERY</h1>
<p class="abs hero-intro">Who we are text Lorem ipsum dolor sit amet, consectetur adipisicing elit, sed do eiusmod tempor incididunt labore dolore magna aliqua. Ut enim ad minim veniam, quis nostrud exercitation ullamco laboris aliquip commodo consequat.</p>

<svg class="abs arrow" style="left:70px;top:424px" viewBox="0 0 14 20"><path d="M11 2 3 10l8 8" fill="none" stroke="#bdbdbd" stroke-width="3"/></svg>
<svg class="abs arrow" style="left:764px;top:424px" viewBox="0 0 14 20"><path d="M3 2l8 8-8 8" fill="none" stroke="#bdbdbd" stroke-width="3"/></svg>

<div class="abs tile" style="left:130px;top:284px;background:linear-gradient(180deg,#6b5a4e,#a07a5c 60%,#3a2e28)" role="img" aria-label="Couple walking hand in hand on a beach at sunset">
  <div class="abs tile-overlay">
    <div class="abs tile-date">20 April 2015</div>
    <div class="abs tile-text">Sed do eiusmod tempor incididunt</div>
    <svg class="abs tile-plus" viewBox="0 0 18 18"><path d="M9 1v16M1 9h16" stroke="#fff" stroke-width="1.6"/></svg>
  </div>
  <svg class="abs heart" viewBox="0 0 16 14"><path d="M8 13 1.6 6.8A3.8 3.8 0 0 1 8 2a3.8 3.8 0 0 1 6.4 4.8z" fill="#fff"/></svg>
</div>

<div class="abs tile" style="left:332px;top:284px;background:linear-gradient(180deg,#8ea2b8,#e8b070 55%,#3b2f2a)" role="img" aria-label="Bride and groom holding hands against a sunset sky">
  <svg class="abs play" viewBox="0 0 30 30"><circle cx="15" cy="15" r="14" fill="rgba(255,255,255,.75)"/><path d="M12 9v12l9-6z" fill="#444"/></svg>
  <div class="abs tile-caption">Sed do eiusmod tempor incididunt</div>
</div>

<div class="abs tile" style="left:534px;top:284px;background:linear-gradient(160deg,#c9a27a,#d9b48a 45%,#8a6e58)" role="img" aria-label="Groom embracing bride with a bouquet by the sea">
  <svg class="abs heart" viewBox="0 0 16 14"><path d="M8 13 1.6 6.8A3.8 3.8 0 0 1 8 2a3.8 3.8 0 0 1 6.4 4.8z" fill="#fff"/></svg>
  <div class="abs tile-caption">Sed do eiusmod tempor incididunt</div>
</div>

<div class="abs tile" style="left:130px;top:441px;background:linear-gradient(180deg,#6f8a4a,#3a2f2a 60%,#1e1a18)" role="img" aria-label="Four bridesmaids in black dresses smiling together">
  <svg class="abs play" viewBox="0 0 30 30"><circle cx="15" cy="15" r="14" fill="rgba(255,255,255,.75)"/><path d="M12 9v12l9-6z" fill="#444"/></svg>
  <div class="abs tile-caption">Sed do eiusmod tempor incididunt</div>
</div>

<div class="abs tile" style="left:332px;top:441px;background:linear-gradient(180deg,#3fa9c9,#7fd0dc 55%,#e8e2d6)" role="img" aria-label="Couple in white running hand in hand on a tropical beach">
  <svg class="abs heart" viewBox="0 0 16 14"><path d="M8 13 1.6 6.8A3.8 3.8 0 0 1 8 2a3.8 3.8 0 0 1 6.4 4.8z" fill="#fff"/></svg>
  <div class="abs tile-caption">Sed do eiusmod tempor incididunt</div>
</div>

<div class="abs tile" style="left:534px;top:441px;background:linear-gradient(180deg,#4a4644,#b9895a 45%,#2a2624)" role="img" aria-label="Bride and groom seen from behind watching a sunset">
  <svg class="abs heart" viewBox="0 0 16 14"><path d="M8 13 1.6 6.8A3.8 3.8 0 0 1 8 2a3.8 3.8 0 0 1 6.4 4.8z" fill="#fff"/></svg>
  <div class="abs tile-caption">Sed do eiusmod tempor incididunt</div>
</div>

<section class="abs social" role="img" aria-label="Dark background with deep red roses"></section>

<h2 class="abs col-title" style="left:128px;top:695px">Social Feeds</h2>
<div class="abs col-rule" style="left:130px;top:729px;width:164px"></div>
<div class="abs col-divider" style="left:317px;top:700px;height:361px"></div>

<div class="abs avatar" style="left:130px;top:750px;background:#a07a60" role="img" aria-label="Profile photo of a man"></div>
<p class="abs feed-text" style="left:182px;top:748px;width:120px">Lorem ipsum dolor sit amet, elit, eiusmod tempor</p>
<span class="abs btn btn-share" style="left:183px;top:778px">Share</span>
<span class="abs btn btn-share" style="left:221px;top:778px">Like</span>
<div class="abs post-photo" style="left:182px;top:798px;background:linear-gradient(180deg,#bdbdbd,#6e6e6e)" role="img" aria-label="Black and white photo of a couple kissing on a beach"></div>
<p class="abs feed-text" style="left:182px;top:865px;width:120px">Lorem ipsum dolor sit amet, elit, sed do eiusmod tempor labore et dolore magna aliqua.</p>
<div class="abs col-rule" style="left:130px;top:933px;width:164px"></div>

<div class="abs avatar" style="left:130px;top:958px;background:#c49c7c" role="img" aria-label="Profile photo of a couple"></div>
<p class="abs feed-text" style="left:182px;top:956px;width:120px">Lorem ipsum dolor sit amet, elit, eiusmod tempor</p>
<span class="abs btn btn-share" style="left:183px;top:986px">Share</span>
<span class="abs btn btn-share" style="left:221px;top:986px">Like</span>
<p class="abs feed-text" style="left:182px;top:1007px;width:120px">Lorem ipsum dolor sit amet, elit, sed do eiusmod tempor labore et dolore magna aliqua.</p>

<h2 class="abs col-title" style="left:340px;top:695px">Latest Posts</h2>
<div class="abs col-rule" style="left:341px;top:729px;width:165px"></div>
<div class="abs col-divider" style="left:536px;top:700px;height:361px"></div>

<div class="abs avatar" style="left:341px;top:750px;background:#b89a86" role="img" aria-label="Profile photo of a smiling couple"></div>
<p class="abs feed-text" style="left:394px;top:748px;width:120px">Lorem ipsum dolor sit amet, elit, eiusmod tempor</p>
<span class="abs btn btn-post" style="left:395px;top:777px">Post</span>
<p class="abs feed-text" style="left:394px;top:796px;width:120px">Lorem ipsum dolor sit amet, elit, sed do eiusmod tempor labore et dolore magna aliqua.</p>
<div class="abs col-rule" style="left:341px;top:868px;width:165px"></div>

<div class="abs avatar" style="left:341px;top:893px;background:#d0b49a" role="img" aria-label="Profile photo of a woman"></div>
<p class="abs feed-text" style="left:394px;top:890px;width:120px">Lorem ipsum dolor sit amet, elit, eiusmod tempor</p>
<span class="abs btn btn-post" style="left:395px;top:920px">Post</span>
<p class="abs feed-text" style="left:394px;top:939px;width:120px">Lorem ipsum dolor sit amet, elit, sed do eiusmod tempor labore et dolore magna aliqua.</p>
<div class="abs post-photo" style="left:394px;top:994px;background:linear-gradient(180deg,#9c9484,#4c463e)" role="img" aria-label="Sepia wedding portrait of a couple"></div>

<h2 class="abs col-title" style="left:562px;top:695px">Photo Stream</h2>
<div class="abs col-rule" style="left:562px;top:729px;width:164px"></div>
<div class="abs" style="left:562px;top:750px;width:79px;height:60px;background:linear-gradient(180deg,#8ea4b4,#6e8a4a)" role="img" aria-label="Bride and groom on a lawn by the water"></div>
<div class="abs" style="left:645px;top:750px;width:81px;height:60px;background:linear-gradient(180deg,#7a6e6e,#3a3232)" role="img" aria-label="Wedding party walking under a tree"></div>
<div class="abs" style="left:562px;top:814px;width:164px;height:174px;background:linear-gradient(180deg,#c8dbe8,#e9e4dc 55%,#d8c8b0)" role="img" aria-label="Bride with bouquet and groom in a beige suit on a beach">
  <div class="abs stream-caption">Sed do eiusmod tempor</div>
</div>
<div class="abs" style="left:562px;top:994px;width:79px;height:59px;background:linear-gradient(180deg,#d8a878,#8a6a50)" role="img" aria-label="Couple on a beach at sunset"></div>
<div class="abs" style="left:645px;top:994px;width:81px;height:59px;background:linear-gradient(180deg,#b8c8a8,#3a3a44)" role="img" aria-label="Portrait of a smiling woman"></div>

<footer class="abs site-footer">
  <nav class="abs footer-nav"><span>Home</span><span>About</span><span>Services</span><span>Media</span><span>Contact</span></nav>
  <div class="abs copyright">© 2015 TendLaneFest</div>
</footer>

</body>
</html>
```